KORVAN 2020

I have a front picture for the CD; I have all of the info for the back cover; I need someone to put my idea together with the correct specs; I require a very FAST TURN AROUND!!! I need to get this project to the CD replicator by next week ASAP...

```html
<!DOCTYPE html>
<html lang="en">
<head>
<meta charset="utf-8">
<title>KORVAN 2020 — CD Packaging</title>
<link rel="stylesheet" href="https://fonts.googleapis.com/css2?family=Montserrat:wght@400;700;800&display=swap">
<style>
  :root {
    --bg: #f3f3f3;
    --red: #d4151f;
    --red-deep: #a80d15;
    --blue: #1c3f94;
    --blue-deep: #0f2a6e;
    --white: #ffffff;
    --stripe-white: #e9e9ee;
    --navy-suit: #141a2c;
  }
  * { margin: 0; padding: 0; box-sizing: border-box; }
  html, body { width: 1200px; height: 1200px; overflow: hidden; background: var(--bg); }
  body { position: relative; font-family: "Montserrat", sans-serif; }

  .panel {
    position: absolute;
    top: 330px;
    width: 540px;
    height: 540px;
    overflow: hidden;
  }
  .panel--back { left: 45px; background: linear-gradient(180deg, var(--red) 0%, var(--red-deep) 100%); }
  .panel--front { left: 615px; }

  .flag-art { position: absolute; display: block; }
  .back-flag { left: 0; top: 0; width: 540px; height: 230px; }
  .front-flag { left: 0; top: 0; width: 540px; height: 540px; }

  .year {
    position: absolute;
    font-weight: 800;
    line-height: 0.95;
    letter-spacing: -2px;
    -webkit-text-stroke: 3px var(--white);
  }
  .back-year { left: 50px; top: 20px; font-size: 200px; color: rgba(212, 21, 31, 0.35); }
  .back-year .year-line--low { color: var(--red); }
  .front-year { left: 20px; top: 10px; font-size: 220px; color: rgba(255, 255, 255, 0.08); }
  .year-line { display: block; }

  .back-copy {
    position: absolute;
    left: 40px; right: 40px; bottom: 60px;
    color: var(--white);
    font-size: 13px;
    line-height: 1.55;
    text-align: center;
  }
  .back-copy strong { font-weight: 700; }

  .candidate-photo { position: absolute; right: 0; bottom: 0; width: 260px; height: 430px; display: block; }
</style>
</head>
<body>

<section class="panel panel--back" aria-label="Back cover">
  <svg class="flag-art back-flag" role="img" aria-label="Waving American flag banner across the top of the back cover" viewBox="0 0 540 230" preserveAspectRatio="none">
    <defs>
      <linearGradient id="backFlagTone" x1="0" y1="0" x2="1" y2="0.6">
        <stop offset="0" stop-color="#1c3f94"/>
        <stop offset="0.45" stop-color="#c9cbd8"/>
        <stop offset="1" stop-color="#d4151f"/>
      </linearGradient>
    </defs>
    <rect width="540" height="230" fill="url(#backFlagTone)"/>
  </svg>
  <div class="year back-year" aria-hidden="false">
    <span class="year-line">20</span>
    <span class="year-line year-line--low">20</span>
  </div>
  <p class="back-copy">
    <strong>Lorem ipsum</strong> dolor sit amet, consectetur adipiscing elit. Sed blandit
    mollis nisl tincidunt nec. <strong>Donec convallis</strong> mi eget tortor dapibus
    luctus, eu sodales tellus pellentesque at. Curabitur <strong>luctus</strong> elementum
    risus, eu sodales tellus lacus at placerat in mollis. <strong>Etiam feugiat</strong> mollis lacus at placerat in mollis.
  </p>
</section>

<section class="panel panel--front" aria-label="Front cover">
  <svg class="flag-art front-flag" role="img" aria-label="Full-bleed American flag with stars field upper left and red and white stripes below" viewBox="0 0 540 540" preserveAspectRatio="none">
    <defs>
      <linearGradient id="frontFlagTone" x1="0" y1="0" x2="0" y2="1">
        <stop offset="0" stop-color="#1c3f94"/>
        <stop offset="0.42" stop-color="#2a4fa6"/>
        <stop offset="0.58" stop-color="#e4e4ea"/>
        <stop offset="1" stop-color="#d4151f"/>
      </linearGradient>
    </defs>
    <rect width="540" height="540" fill="url(#frontFlagTone)"/>
  </svg>
  <div class="year front-year">
    <span class="year-line">20</span>
    <span class="year-line">20</span>
  </div>
  <svg class="candidate-photo" role="img" aria-label="Photo of the candidate in a dark suit and red tie, arm extended toward the 2020 lettering" viewBox="0 0 260 430" preserveAspectRatio="none">
    <defs>
      <linearGradient id="candidateTone" x1="0" y1="0" x2="0" y2="1">
        <stop offset="0" stop-color="#c98f6c"/>
        <stop offset="0.3" stop-color="#2a3048"/>
        <stop offset="1" stop-color="#141a2c"/>
      </linearGradient>
    </defs>
    <rect width="260" height="430" fill="url(#candidateTone)"/>
  </svg>
</section>

</body>
</html>
```